Banner design

Hello.
I require a top header banner for my Interactive and electronic whiteboard / Audio Visual business.
Animated gif.

http://www.qorvantix.com.au

Basically a few photos, my phone number and my new logo (coming soon "Palquestron")
Corporate looking, that immediately captures the customers attention.

Target Market(s)

Adults in Western speaking country (Australia). To young business professionals, teachers, managers etc

Industry/Entity Type

Electronic

```html
<!DOCTYPE html>
<html lang="en">
<head>
<meta charset="utf-8">
<title>Palquestron header banner</title>
<link href="https://fonts.googleapis.com/css2?family=Arimo:wght@400;700&display=swap" rel="stylesheet">
<style>
  :root {
    --ink: #111111;
    --brand-red: #d81e2c;
    --band-white: rgba(255, 255, 255, 0.85);
    --band-fade: rgba(255, 255, 255, 0.5);
    --contact-white: #ffffff;
    --board-magenta: #c2307e;
    --board-pink: #e86aa8;
    --board-orange: #f0873a;
    --room-red: #d41c20;
    --room-light: #f6c6a8;
    --room-orange: #e8602e;
    --pupil-deep: #6a0c10;
    --pupil-red: #b0151c;
    --pupil-pink: #e0338f;
  }
  * { margin: 0; padding: 0; box-sizing: border-box; }
  html, body { width: 1200px; height: 318px; overflow: hidden; background: #ffffff; }
  .banner {
    position: relative;
    width: 1200px;
    height: 318px;
    overflow: hidden;
    font-family: "Arimo", Arial, sans-serif;
    background: var(--room-red);
  }
  .photo { position: absolute; top: 0; height: 318px; }
  .photo--whiteboard {
    left: 0;
    width: 380px;
    background:
      radial-gradient(ellipse 90px 110px at 220px 190px, rgba(255,235,235,0.55), transparent 70%),
      linear-gradient(100deg, var(--board-magenta) 0%, var(--board-pink) 30%, var(--board-orange) 58%, var(--board-magenta) 78%, var(--room-red) 100%);
    -webkit-mask-image: linear-gradient(90deg, #000 82%, transparent 100%);
    mask-image: linear-gradient(90deg, #000 82%, transparent 100%);
  }
  .photo--classroom {
    left: 330px;
    width: 380px;
    background:
      radial-gradient(ellipse 120px 90px at 240px 100px, var(--room-light), transparent 75%),
      radial-gradient(ellipse 80px 110px at 100px 210px, rgba(255,140,90,0.7), transparent 75%),
      linear-gradient(180deg, var(--room-orange) 0%, var(--room-red) 55%, #9c1016 100%);
    -webkit-mask-image: linear-gradient(90deg, transparent 0%, #000 14%, #000 84%, transparent 100%);
    mask-image: linear-gradient(90deg, transparent 0%, #000 14%, #000 84%, transparent 100%);
  }
  .photo--pupil {
    left: 650px;
    width: 550px;
    background:
      radial-gradient(ellipse 110px 100px at 140px 150px, rgba(240,140,110,0.55), transparent 75%),
      radial-gradient(ellipse 130px 90px at 470px 90px, rgba(255,210,90,0.55), transparent 75%),
      linear-gradient(90deg, var(--pupil-red) 0%, var(--pupil-deep) 35%, var(--pupil-red) 60%, var(--pupil-pink) 82%, #b01f5c 100%);
    -webkit-mask-image: linear-gradient(90deg, transparent 0%, #000 10%);
    mask-image: linear-gradient(90deg, transparent 0%, #000 10%);
  }
  .banner__band {
    position: absolute;
    left: 0;
    top: 37px;
    width: 1200px;
    height: 58px;
    background: linear-gradient(90deg, var(--band-white) 0%, var(--band-white) 40%, var(--band-fade) 100%);
  }
  .brand {
    position: absolute;
    left: 20px;
    top: 41px;
    display: flex;
    align-items: center;
    gap: 14px;
  }
  .brand__mark {
    width: 26px;
    height: 26px;
    border-radius: 50%;
    background: var(--brand-red);
  }
  .brand__name {
    font-weight: 700;
    font-size: 44px;
    letter-spacing: -1.5px;
    color: var(--ink);
    line-height: 50px;
  }
  .contact {
    position: absolute;
    right: 18px;
    top: 250px;
    text-align: right;
    color: var(--contact-white);
    font-size: 18px;
    line-height: 22px;
  }
</style>
</head>
<body>
  <header class="banner">
    <div class="photo photo--whiteboard" role="img" aria-label="Photo: children drawing on a colourful interactive whiteboard with a stylus"></div>
    <div class="photo photo--classroom" role="img" aria-label="Photo: classroom with a student pointing at a projected road scene on a whiteboard"></div>
    <div class="photo photo--pupil" role="img" aria-label="Photo: smiling pupil reaching up to touch an interactive whiteboard"></div>
    <div class="banner__band"></div>
    <div class="brand">
      <span class="brand__mark"></span>
      <span class="brand__name">Palquestron</span>
    </div>
    <div class="contact">
      <p class="contact__email">mail@palquestron.com.au</p>
      <p class="contact__phone">0412 555 019 or (02) 5550 1847</p>
    </div>
  </header>
</body>
</html>
```